Design a styled business card for an intimacy and attachment psychologist

I am a Psychologist providing online therapy to patients across the United States. My work is interpersonal and emotion-focused, with an emphasis on the client-therapist relationship. My primary areas of work are very personal, including sexuality and gender, abuse and trauma, and grief and loss. My target audience will be adults of all ages 18+.
My business card should convey a warm and inviting feeling of professionalism that is also casual and comfortable.
The front should be fairly simple and professional, consisting of:
- My name, Dr. Rosalind Petrakis
- My title, Licensed Psycholigist
- My logo
On either the front or the back, my contact information should be listed:
- ros@drrospetrakis.example
- 555.014.7788
- drrospetrakis.example
On the rear, I would like a description of the areas that I specialize in. This can be formatted in any way that appears stylistically interesting.
Individual and Couples
Relationships and Infidelity
Sexual Health & Aging
Gender Identity & Sexual Orientation
Abuse and Trauma
Sexual Compulsivity & Addiction
Sexual Dysfunction
Target Market(s)
My target audience will be adults of all ages 18+.
Industry/Entity Type
Psychology
Contact Information for Business Card
The front should be fairly simple and professional, consisting of: - My name, Dr. Rosalind Petrakis - My title, Licensed Psycholigist - My logo On either the front or the back, my contact information should be listed: - ros@drrospetrakis.example - 555.014.7788 - drrospetrakis.example On the rear, I would like a description of the areas that I specialize in. This can be formatted in any way that appears stylistically interesting. Individual and Couples Relationships and Infidelity Sexual Health & Aging Gender Identity & Sexual Orientation Abuse and Trauma Sexual Compulsivity & Addiction Sexual Dysfunction
- Follow brand guide

```html
<!DOCTYPE html>
<html lang="en">
<head>
<meta charset="utf-8">
<title>Dr. Rosalind Petrakis — Business Card</title>
<link rel="stylesheet" href="https://fonts.googleapis.com/css2?family=Montserrat:wght@400;500;700&display=swap">
<style>
  :root {
    --teal: #5fc3a9;
    --teal-light: #a3dccd;
    --red: #e8423f;
    --gold: #f5a623;
    --navy: #2a2550;
    --white: #ffffff;
    --backdrop: #e9ecea;
  }
  * { margin: 0; padding: 0; box-sizing: border-box; }
  html, body { width: 1200px; height: 900px; overflow: hidden; }
  body {
    background: var(--backdrop);
    font-family: "Montserrat", sans-serif;
    display: flex;
    flex-direction: column;
    align-items: center;
    justify-content: center;
    gap: 40px;
  }
  .card {
    position: relative;
    width: 700px;
    height: 400px;
    overflow: hidden;
    box-shadow: 0 6px 18px rgba(0,0,0,0.18);
  }

  /* Specialties side */
  .card--specialties { background: var(--teal); }
  .brand-mark {
    position: absolute;
    left: 40px;
    top: 80px;
    width: 240px;
    height: 240px;
    border-radius: 50%;
    border: 9px solid var(--navy);
    background: var(--teal-light);
    display: flex;
    align-items: center;
    justify-content: center;
    text-align: center;
    padding: 30px;
  }
  .brand-mark__name {
    color: var(--navy);
    font-weight: 700;
    font-size: 24px;
    line-height: 1.25;
    text-transform: uppercase;
    letter-spacing: 1px;
  }
  .divider {
    position: absolute;
    left: 318px;
    top: 70px;
    width: 260px;
    height: 260px;
  }
  .specialty-list {
    position: absolute;
    left: 350px;
    top: 72px;
    list-style: none;
    color: var(--white);
    font-size: 17px;
    font-weight: 500;
    line-height: 32px;
  }
  .specialty-list li { display: flex; align-items: center; gap: 10px; }
  .specialty-list li.continued { padding-left: 28px; }
  .tick { width: 18px; height: 18px; flex: none; }

  /* Contact side */
  .card--contact { background: var(--white); }
  .wave { position: absolute; inset: 0; width: 100%; height: 100%; }
  .lockup {
    position: absolute;
    left: 60px;
    top: 70px;
    display: flex;
    align-items: center;
    gap: 16px;
  }
  .lockup__circle {
    width: 64px;
    height: 64px;
    border-radius: 50%;
    background: var(--teal);
    flex: none;
  }
  .lockup__name {
    color: var(--navy);
    font-weight: 700;
    font-size: 26px;
    line-height: 1.1;
    text-transform: uppercase;
    letter-spacing: 1px;
  }
  .contact {
    position: absolute;
    right: 36px;
    top: 200px;
    text-align: right;
    color: var(--white);
  }
  .contact__name { font-weight: 700; font-size: 19px; letter-spacing: 0.5px; }
  .contact__title { font-size: 15px; margin-bottom: 12px; }
  .contact__row {
    display: flex;
    justify-content: flex-end;
    align-items: center;
    gap: 10px;
    font-size: 14px;
    line-height: 26px;
  }
  .contact__icon { width: 16px; height: 16px; flex: none; }
</style>
</head>
<body>

<section class="card card--specialties" aria-label="Areas of specialty">
  <div class="brand-mark"><span class="brand-mark__name">Dr. Rosalind Petrakis</span></div>
  <svg class="divider" viewBox="0 0 260 260" aria-hidden="true">
    <line x1="4" y1="0" x2="4" y2="260" stroke="var(--gold)" stroke-width="2"/>
    <line x1="12" y1="20" x2="12" y2="240" stroke="var(--gold)" stroke-width="2"/>
    <line x1="20" y1="40" x2="20" y2="220" stroke="var(--gold)" stroke-width="2"/>
  </svg>
  <ul class="specialty-list">
    <li><svg class="tick" viewBox="0 0 18 18" aria-hidden="true"><circle cx="9" cy="9" r="7.5" fill="none" stroke="var(--gold)" stroke-width="2"/><path d="M5 9l3 3 6-7" fill="none" stroke="var(--gold)" stroke-width="2.4" stroke-linecap="round" stroke-linejoin="round"/></svg>Individual and Couples</li>
    <li><svg class="tick" viewBox="0 0 18 18" aria-hidden="true"><circle cx="9" cy="9" r="7.5" fill="none" stroke="var(--gold)" stroke-width="2"/><path d="M5 9l3 3 6-7" fill="none" stroke="var(--gold)" stroke-width="2.4" stroke-linecap="round" stroke-linejoin="round"/></svg>Relationships and Infidelity</li>
    <li><svg class="tick" viewBox="0 0 18 18" aria-hidden="true"><circle cx="9" cy="9" r="7.5" fill="none" stroke="var(--gold)" stroke-width="2"/><path d="M5 9l3 3 6-7" fill="none" stroke="var(--gold)" stroke-width="2.4" stroke-linecap="round" stroke-linejoin="round"/></svg>Sexual Health &amp; Aging</li>
    <li><svg class="tick" viewBox="0 0 18 18" aria-hidden="true"><circle cx="9" cy="9" r="7.5" fill="none" stroke="var(--gold)" stroke-width="2"/><path d="M5 9l3 3 6-7" fill="none" stroke="var(--gold)" stroke-width="2.4" stroke-linecap="round" stroke-linejoin="round"/></svg>Gender Identity &amp;</li>
    <li class="continued">Sexual Orientation</li>
    <li><svg class="tick" viewBox="0 0 18 18" aria-hidden="true"><circle cx="9" cy="9" r="7.5" fill="none" stroke="var(--gold)" stroke-width="2"/><path d="M5 9l3 3 6-7" fill="none" stroke="var(--gold)" stroke-width="2.4" stroke-linecap="round" stroke-linejoin="round"/></svg>Abuse and Trauma</li>
    <li><svg class="tick" viewBox="0 0 18 18" aria-hidden="true"><circle cx="9" cy="9" r="7.5" fill="none" stroke="var(--gold)" stroke-width="2"/><path d="M5 9l3 3 6-7" fill="none" stroke="var(--gold)" stroke-width="2.4" stroke-linecap="round" stroke-linejoin="round"/></svg>Sexual Compulsivity &amp; Addiction</li>
    <li><svg class="tick" viewBox="0 0 18 18" aria-hidden="true"><circle cx="9" cy="9" r="7.5" fill="none" stroke="var(--gold)" stroke-width="2"/><path d="M5 9l3 3 6-7" fill="none" stroke="var(--gold)" stroke-width="2.4" stroke-linecap="round" stroke-linejoin="round"/></svg>Sexual Dysfunction</li>
  </ul>
</section>

<section class="card card--contact" aria-label="Contact details">
  <svg class="wave" viewBox="0 0 700 400" preserveAspectRatio="none" aria-hidden="true">
    <path d="M0,330 C200,315 280,250 330,150 C380,50 560,18 700,12 L700,400 L0,400Z" fill="var(--teal)"/>
    <path d="M0,338 C205,323 285,258 335,158 C385,58 565,26 700,20 L700,400 L0,400Z" fill="var(--white)"/>
    <path d="M0,345 C210,330 290,265 340,165 C390,65 570,33 700,27 L700,400 L0,400Z" fill="var(--red)"/>
    <path d="M0,366 C222,351 302,286 352,186 C402,86 582,54 700,48 L700,400 L0,400Z" fill="var(--white)"/>
    <path d="M0,372 C227,357 307,292 357,192 C407,92 587,60 700,54 L700,400 L0,400Z" fill="var(--teal)"/>
  </svg>

  <div class="lockup">
    <span class="lockup__circle"></span>
    <span class="lockup__name">Dr. Rosalind<br>Petrakis</span>
  </div>

  <div class="contact">
    <p class="contact__name">DR. ROSALIND PETRAKIS</p>
    <p class="contact__title">Licensed Psycholigist</p>
    <p class="contact__row">555.014.7788
      <svg class="contact__icon" viewBox="0 0 16 16" aria-hidden="true"><path d="M3 2h3l1 4-2 1c1 2 2 3 4 4l1-2 4 1v3c0 1-1 1-1 1C7 14 2 9 2 3c0 0 0-1 1-1z" fill="var(--white)"/></svg>
    </p>
    <p class="contact__row">ros@drrospetrakis.example
      <svg class="contact__icon" viewBox="0 0 16 16" aria-hidden="true"><rect x="1" y="3" width="14" height="10" fill="var(--white)"/><path d="M1 3l7 6 7-6" fill="none" stroke="var(--teal)" stroke-width="1.5"/></svg>
    </p>
    <p class="contact__row">www.drrospetrakis.example
      <svg class="contact__icon" viewBox="0 0 16 16" aria-hidden="true"><circle cx="8" cy="8" r="7" fill="var(--white)"/><path d="M1 8h14M8 1c-3 3-3 11 0 14M8 1c3 3 3 11 0 14" fill="none" stroke="var(--teal)" stroke-width="1.2"/></svg>
    </p>
  </div>
</section>

</body>
</html>
```